Verpackungsdesign für Pasta aus Buchweizen
Zielgruppe
Unser Unternehmen KORNIVA sucht ein sehr modernes Verpackungsdesign für Pasta aus Buchweizen.
Unsere Produkte sind in unserem Online Shop und unterscheiden sich durch die herkömmliche Pasta, da wir Buchweizen in die Verarbeitung mit aufnehmen und somit die gesundheitsfördernde Eigenschaft des Buchweizens im Vordergrund steht. Unsere Pasta aus Buchweizenmehl mit klassischem Hartweizengrieß ist in dieser Form noch nicht im stationären Handel erhältlich, deshalb wünschen wir uns ein neues, ansprechendes Verpackungsdesign welches von den Massenprodukten aus den Regalen im Handel heraussticht. Das Design sollte also minimalistisch und sehr modern wirken, und sich deutlich von der Konkurrenz abheben.
Die Zielgruppe richtet sich sowohl an Massen die Pasta in allen Variationen lieben, als auch an ernährungsbewusste Veganer/Vegetarier die Alternativen im Bereich der herkömmlichen Pasta Kochkultur suchen.
PS: Mit dem Verkauf unserer Pasta investieren wir außerdem in den Aufbau und der Infrastruktur des Erzeugerlandes. Durch unser Prinzip „Teilen & Wachsen“ fördern wir mit unseren Gewinnen nachhaltige Projekte in den Erzeugerländern und helfen somit wirtschaftlich benachteiligten Regionen auf der Welt. (Fair Trade)
Aufgabenstellung
Wir besitzen bereits ein Logo und Verpackungen für unsere Pasta Sorten. Das Logo und das Grundgerüst der Stanzform / Verpackungsmaße (inkl. Sichtfenster) soll beibehalten werden (Siehe Anhang). Als Pasta Verpackungen benutzen wir Faltschachteln und Banderolen.
Verpackungsmaße:
- Faltschachtel (90 x 40 x 165 mm)
- Banderole (560 x 70mm)
Der Produktname ist je nach Sorte zu präzisieren:
- Fusilli
- Makkaroni
- Bandnudeln
- Tarhana
Produktgewicht:
- 250g
Eigenschaften:
- Buchweizenmehl
- 100% Vegan
- Kochzeit 3 Minuten
- Liebevolle Handarbeit
WICHTIG:
1) Bitte benutzt die hochgeladene, leere Stanzform für Artwork.
2) Die Designfarbe kann anhand des Aufstellers ausgerichtet werden (CMYK: 0, 20, 32, 0 und 60, 57, 56, 62) es ist aber kein muss und ihr seit frei in der Kreativität.
3) Bitte das Sichtfenster mit Rand wie aktuell auf den Produkten übernehmen (siehe www.korniva.de/shop)
Nach dem Wettbewerb planen wir zusätzlich ein 1zu1 Projekt und würden uns freuen einen Gewinner auszuwählen - Wir freuen uns auf eure Ideen :)

```html
<!DOCTYPE html>
<html lang="de">
<head>
<meta charset="utf-8">
<title>KORNIVA Buchweizen Pasta – Faltschachtel</title>
<link rel="stylesheet" href="https://fonts.googleapis.com/css2?family=Anton&family=Oswald:wght@500;600&family=Lato:wght@300;400&family=Libre+Baskerville&display=swap">
<style>
  :root {
    --bg: #cdcdcd;
    --paper: #ffffff;
    --clay: #9c746a;
    --cocoa: #6b4a43;
    --ink: #111111;
    --pasta-light: #b98a5e;
    --pasta-dark: #6e4a2c;
    --vegan: #5aa53a;
    --script: #e4e0dd;
  }
  * { margin: 0; padding: 0; box-sizing: border-box; }
  html, body { width: 1200px; height: 1148px; overflow: hidden; }
  body { background: var(--bg); font-family: "Lato", sans-serif; position: relative; }

  .dieline { position: absolute; top: 124px; left: 245px; height: 900px; display: flex; box-shadow: 0 18px 40px rgba(0,0,0,.18); }

  /* side panel */
  .side-panel { width: 218px; height: 900px; background: var(--paper); position: relative; }
  .side-panel__cooking { position: absolute; top: 190px; left: 0; right: 0; text-align: center; font-weight: 300; font-size: 18px; line-height: 21px; letter-spacing: .5px; color: #333; text-transform: uppercase; }
  .side-panel__band { position: absolute; top: 232px; left: 0; right: 0; bottom: 0; background: var(--clay); }
  .pot-icon { position: absolute; top: 42px; left: 50%; transform: translateX(-50%); width: 92px; height: 100px; }
  .side-panel__copy { position: absolute; top: 210px; left: 22px; right: 22px; font-size: 8.5px; line-height: 11px; color: #3b2924; text-align: justify; }
  .side-panel__copy p + p { margin-top: 14px; }
  .vegan-badge { position: absolute; bottom: 118px; left: 50%; transform: translateX(-50%); width: 46px; height: 46px; border-radius: 50%; background: var(--vegan); border: 3px solid #fff; }
  .net-weight { position: absolute; bottom: 44px; left: 0; right: 0; text-align: center; font-size: 16px; font-weight: 300; color: #2c1f1b; }

  /* front panel */
  .front-panel { width: 491px; height: 900px; background: var(--paper); position: relative; overflow: hidden; }
  .front-panel__art { position: absolute; inset: 0; }

  .brand-mark { position: absolute; top: 86px; left: 0; right: 0; display: flex; justify-content: center; align-items: center; gap: 10px; }
  .brand-mark__dot { width: 14px; height: 14px; border-radius: 50%; background: var(--cocoa); }
  .brand-mark__name { font-family: "Oswald", sans-serif; font-weight: 600; font-size: 30px; letter-spacing: 1px; color: var(--cocoa); }

  .product-kicker { position: absolute; top: 176px; left: 100px; width: 260px; text-align: center; font-family: "Oswald", sans-serif; font-weight: 600; font-size: 38px; line-height: 44px; letter-spacing: 2px; color: var(--ink); }
  .product-title { position: absolute; top: 226px; left: 96px; font-family: "Anton", sans-serif; font-size: 128px; line-height: 140px; letter-spacing: -3px; color: var(--ink); transform: scaleX(.86); transform-origin: left top; white-space: nowrap; }
  .product-subtitle { position: absolute; top: 374px; left: 190px; width: 180px; height: 46px; background: var(--script); border-radius: 4px; }

  .variety { position: absolute; left: 45px; top: 560px; transform: translate(-50%, -50%) rotate(-90deg); font-family: "Libre Baskerville", serif; font-size: 22px; color: #fff; letter-spacing: 1px; white-space: nowrap; }
</style>
</head>
<body>

<div class="dieline">
  <section class="side-panel">
    <div class="side-panel__cooking">Kochzeit<br>3 Minuten</div>
    <div class="side-panel__band">
      <svg class="pot-icon" viewBox="0 0 92 100" fill="none" stroke="#111" stroke-width="2.4" stroke-linecap="round" stroke-linejoin="round" aria-hidden="true">
        <path d="M14 30 h48 v30 a10 10 0 0 1 -10 10 h-28 a10 10 0 0 1 -10 -10 z"/>
        <path d="M10 30 h56"/>
        <path d="M14 38 h-8 M62 38 h8"/>
        <path d="M30 30 q8 -12 16 0"/>
        <path d="M19 52 q5 -5 10 0 q5 5 10 0 q5 -5 10 0 q5 5 10 0"/>
        <path d="M72 22 q8 -4 4 -10 q-4 -6 4 -10 M66 26 q6 -2 4 -7"/>
        <path d="M26 84 q-3 5 0 7 q3 -2 0 -7 M38 84 q-3 5 0 7 q3 -2 0 -7 M50 84 q-3 5 0 7 q3 -2 0 -7"/>
      </svg>
      <div class="side-panel__copy">
        <p>Pasta aus Buchweizenmehl und Hartweizengrieß, in liebevoller Handarbeit hergestellt.</p>
        <p>In reichlich kochendem Salzwasser drei Minuten garen, abgießen und nach Belieben mit Soße oder Gemüse servieren.</p>
        <p>Zutaten: Buchweizenmehl, Hartweizengrieß, Wasser. Kann Spuren von Soja und Senf enthalten. Trocken und kühl lagern. Mit jedem Kauf fördern wir nachhaltige Projekte in den Erzeugerländern.</p>
      </div>
      <div class="vegan-badge" aria-hidden="true"></div>
      <div class="net-weight">250g ℮</div>
    </div>
  </section>

  <section class="front-panel">
    <svg class="front-panel__art" viewBox="0 0 491 900">
      <defs>
        <linearGradient id="pasta-tone" x1="0" y1="0" x2="1" y2="1">
          <stop offset="0" stop-color="#b98a5e"/>
          <stop offset="1" stop-color="#6e4a2c"/>
        </linearGradient>
      </defs>
      <rect class="variety-band" x="0" y="232" width="96" height="668" fill="#9c746a"/>
      <rect class="accent-rule" x="96" y="232" width="13" height="668" fill="#111111"/>
      <g class="viewing-windows" role="img" aria-label="Sichtfenster in Blattform mit Blick auf Buchweizen-Fusilli">
        <path d="M190 508 C250 560 250 640 208 672 C160 640 140 570 190 508 Z" fill="url(#pasta-tone)"/>
        <path d="M0 648 C60 640 130 665 140 705 C110 760 40 765 0 740 Z" fill="url(#pasta-tone)"/>
        <path d="M302 652 C300 720 260 780 176 792 C170 720 220 670 302 652 Z" fill="url(#pasta-tone)"/>
      </g>
    </svg>
    <div class="brand-mark">
      <span class="brand-mark__dot"></span>
      <span class="brand-mark__name">KORNIVA</span>
    </div>
    <div class="product-kicker">BUCHWEIZEN</div>
    <div class="product-title">PASTA</div>
    <div class="product-subtitle" role="img" aria-label="Handgeschriebener Schriftzug Buckwheat"></div>
    <div class="variety">fusilli</div>
  </section>
</div>

</body>
</html>
```